Bright Harbor Design

We need a web design for our startup company based in Zurich, Switzerland called Bright Harbor. We offer professional flirt and dating advice, self development with seminars and practical coachings.

The final website aims for two capital goals. First, it will contain text, pictures and video based content presenting and advertising our services. Furthermore, we want to bind our costumers with a plattform offering them to share their expiriences related with our services.

The targeted group will be men from 25 to 40 years.
Updates

The design requires also a register-box to put in the clients Name and Email

I need (besides of the "email registration box") a "Video Gallery", "Blog" and "Agenda (with the next events to come)"

Target Market(s)

Guys around 25 to 40 years who want to improve their social lifestyle

Industry/Entity Type

Advertising

Requirements
Must have
• First and foremost, the design must transfer strong emotions and suggest an attractive social lifestyle.

The design should not be overloaded with content but should include pictures, videos and text.

The design should present a modern, urban lifestyle.
Nice to have
• There is a logo attached to the assignement. However, if you have a good idea for an improved or different logo, please do not hesitate to design your ideas.

```html
<!DOCTYPE html>
<html lang="en">
<head>
<meta charset="utf-8">
<title>Bright Harbor – Home</title>
<link rel="stylesheet" href="https://fonts.googleapis.com/css2?family=Ubuntu:ital,wght@0,400;0,500;1,400&display=swap">
<style>
:root{
  --header-top:#2c2c2c;
  --header-bottom:#0f0f0f;
  --nav-text:#a8a8a8;
  --nav-active:#ffffff;
  --accent:#f2515c;
  --accent-light:#f7757c;
  --heading:#4a4a4a;
  --body-text:#7a7a7a;
  --page:#ffffff;
}
*{margin:0;padding:0;box-sizing:border-box}
html,body{width:1200px;height:1000px;overflow:hidden}
body{position:relative;background:var(--page);font-family:"Ubuntu",sans-serif;color:var(--body-text)}
h2,h3{font-weight:400}
.abs{position:absolute}

/* header */
.site-header{left:0;top:0;width:1200px;height:68px;background:linear-gradient(var(--header-top),var(--header-bottom));border-bottom:1px solid #000}
.brand{left:130px;top:12px;display:flex;align-items:center;gap:10px;color:#fff;font-size:17px;font-weight:500;line-height:1}
.brand-dot{width:34px;height:34px;border-radius:50%;background:#fff}
.main-nav a{position:absolute;top:28px;font-size:14px;color:var(--nav-text);text-decoration:none}
.main-nav .is-active{left:313px;top:0;width:91px;height:68px;background:linear-gradient(#4a4a4a,#262626);border-left:1px solid #555;border-right:1px solid #000;color:var(--nav-active);font-size:15px;text-align:center;padding-top:26px}
.user-box{left:906px;top:0;width:162px;height:68px;background:linear-gradient(#555,#2a2a2a);border-left:1px solid #666}
.user-avatar{left:7px;top:7px;width:52px;height:52px;background:linear-gradient(#8a8f96,#5a5f66)}
.user-greeting{left:66px;top:16px;color:#fff;font-size:13px;font-weight:500}
.user-settings{left:66px;top:37px;color:#fff;font-size:10px}

/* hero */
.hero{left:0;top:68px;width:1200px;height:500px}
.hero-photo{left:0;top:0;width:1200px;height:470px;background:linear-gradient(100deg,#6b5840 0%,#3b2f25 35%,#5a4a68 60%,#8a5440 85%,#c9a26a 100%)}
.hero-curve{left:0;top:0}
.hero-caption{left:130px;top:329px;color:#fff;font-size:19.5px;font-weight:500;line-height:25px;text-shadow:0 1px 2px rgba(0,0,0,.5)}
.hero-arrow{top:402px;width:48px;height:62px;border:1px solid rgba(255,255,255,.35);background:rgba(255,255,255,.08);color:#fff;font-size:22px;text-align:center;line-height:58px}

/* articles */
.post-title{color:var(--heading);font-size:19px;line-height:23px}
.byline{color:var(--accent);font-size:11.5px;font-style:italic}
.post-text{font-size:12px;line-height:15.4px}
.read-more{width:77px;height:23px;background:linear-gradient(var(--accent-light),var(--accent));border-radius:2px;color:#fff;font-size:11px;font-style:italic;padding:4px 9px}
.thumb{background:linear-gradient(135deg,#cfe3ea,#8fb7c6 60%,#e7c9a4)}

/* sidebar */
.side-heading{color:var(--heading);font-size:20px}
.review-photo{width:80px;height:83px;background:linear-gradient(#c79a7a,#8a5a3a)}
.review-text{width:205px;font-size:12px;line-height:15.4px}
</style>
</head>
<body>

<header class="site-header abs">
  <div class="brand abs"><span class="brand-dot"></span>bright harbor</div>
  <nav class="main-nav">
    <a class="is-active" href="#">Home</a>
    <a style="left:431px" href="#">About</a>
    <a style="left:507px" href="#">Join</a>
    <a style="left:580px" href="#">Blog</a>
    <a style="left:649px" href="#">Dating 101</a>
    <a style="left:754px" href="#">Contact</a>
  </nav>
  <div class="user-box abs">
    <div class="user-avatar abs" role="img" aria-label="Member profile photo"></div>
    <div class="user-greeting abs">Hello McUser</div>
    <div class="user-settings abs">Settings ▾</div>
  </div>
</header>

<section class="hero abs">
  <div class="hero-photo abs" role="img" aria-label="Photo of a man and a woman talking in a colourful home goods shop"></div>
  <svg class="hero-curve abs" width="1200" height="500" viewBox="0 0 1200 500">
    <path d="M0 369 Q600 560 1200 313 L1200 500 L0 500 Z" fill="var(--accent)"/>
    <path d="M0 392 Q600 575 1200 328" fill="none" stroke="#f9959a" stroke-width="3" opacity=".6"/>
    <path d="M0 437 Q560 560 1200 335 L1200 500 L0 500 Z" fill="#ffffff"/>
  </svg>
  <p class="hero-caption abs">This is Brightdraft's version&nbsp; of Lorem Ipsum.<br>Proin gravida</p>
  <div class="hero-arrow abs" style="left:121px">‹</div>
  <div class="hero-arrow abs" style="left:169px">›</div>
</section>

<article>
  <h2 class="post-title abs" style="left:131px;top:575px;width:615px">Dating advice from a married man who hopes you don't waste as much of your single life as he did.</h2>
  <p class="byline abs" style="left:131px;top:627px">by Jeff McUser on Jan 14, 2013</p>
  <p class="post-text abs" style="left:130px;top:651px;width:622px">This is Brightdraft's version&nbsp; of Lorem Ipsum. Proin gravida nibh vel velit auctor aliquet. Aenean sollicitudin, lorem quis bibendum auctor, nisi elit consequat ipsum, nec sagittis sem nibh id elit. Duis sed odio sit amet nibh vulputate cursus a sit amet mauris. Morbi accumsan ipsum velit. Nam nec tellus a odio tincidunt auctor a ornare odio. Sed non&nbsp; mauris vitae erat consequat auctor eu in elit. Class aptent taciti sociosqu ad litora torquent per conubia nostra, per inceptos himenaeos. Mauris in erat justo. Nullam ac urna eu felis dapibus condimentum sit amet a augue. Sed non neque elit. Sed ut imperdiet nisi. Proin condimentum fermentum nunc. Etiam pharetra, erat sed fermentum feugiat, velit mauris egestas quam, ut aliquam massa nisl quis neque. Suspendisse in orci enim.</p>
  <a class="read-more abs" style="left:129px;top:768px">read more</a>
</article>

<article>
  <div class="thumb abs" style="left:130px;top:832px;width:150px;height:136px" role="img" aria-label="Photo of a smiling woman holding a card"></div>
  <h2 class="post-title abs" style="left:287px;top:826px;font-size:20px">How To Handle An Intimidating Woman</h2>
  <p class="byline abs" style="left:289px;top:852px">by Jeff McUser on Jan 14, 2013</p>
  <p class="post-text abs" style="left:289px;top:877px;width:452px;height:62px;overflow:hidden">This is Brightdraft's version&nbsp; of Lorem Ipsum. Proin gravida nibh vel velit auctor aliquet. Aenean sollicitudin, lorem quis bibendum auctor, nisi elit consequat ipsum, nec sagittis sem nibh id elit. Duis sed odio sit amet nibh vulputate cursus a sit amet mauris. Morbi accumsan ipsum velit. Nam nec tellus a odio tincidunt auctor a ornare odio.</p>
  <a class="read-more abs" style="left:288px;top:945px">read more</a>
</article>

<aside>
  <h3 class="side-heading abs" style="left:771px;top:575px">Reviews</h3>

  <div class="review-photo abs" style="left:770px;top:617px" role="img" aria-label="Reviewer portrait"></div>
  <p class="review-text abs" style="left:858px;top:614px;height:62px;overflow:hidden">This is Brightdraft's version&nbsp; of Lorem Ipsum. Proin gravida nibh vel velit auctor aliquet. Aenean sollicitudin, lorem quis bibendum auctor, nisi elit consequat ipsum.</p>
  <p class="byline abs" style="left:858px;top:684px">by Jeff McUser on Jan 14, 2013</p>

  <div class="review-photo abs" style="left:770px;top:723px" role="img" aria-label="Reviewer portrait"></div>
  <p class="review-text abs" style="left:858px;top:720px;height:62px;overflow:hidden">This is Brightdraft's version&nbsp; of Lorem Ipsum. Proin gravida nibh vel velit auctor aliquet. Aenean sollicitudin, lorem quis bibendum auctor, nisi elit consequat ipsum.</p>
  <p class="byline abs" style="left:858px;top:790px">by Jeff McUser on Jan 14, 2013</p>

  <div class="review-photo abs" style="left:770px;top:831px" role="img" aria-label="Reviewer portrait"></div>
  <p class="review-text abs" style="left:858px;top:828px;height:62px;overflow:hidden">This is Brightdraft's version&nbsp; of Lorem Ipsum. Proin gravida nibh vel velit auctor aliquet. Aenean sollicitudin, lorem quis bibendum auctor, nisi elit consequat ipsum.</p>
  <p class="byline abs" style="left:858px;top:898px">by Jeff McUser on Jan 14, 2013</p>

  <h3 class="side-heading abs" style="left:771px;top:944px">Videos</h3>
  <div class="abs" style="left:770px;top:983px;width:139px;height:30px;background:linear-gradient(#6a4a4a,#3a2a2a)" role="img" aria-label="Video thumbnail"></div>
  <p class="abs" style="left:917px;top:979px;color:var(--heading);font-size:14px">It's not about getting</p>
</aside>

</body>
</html>
```